依頼詳細
頂いている参考サイトとしては下記のURLがありますが、
先方でもどのデザインの何が良いのかは計りかねているらしく、
下記を参考に様々な形式でデザインを作成して欲しいということです。

‣BRIGHTLEAF https://www.brightleaf57.jp/biwako-sup/ ➡デザインが素敵
‣丸岡商 https://www.maruokasho.co.jp/ja/ ➡ 大企業感
‣ひらめき工房本部 https://www.hiramekikobo.jp/  ➡ 同コンセプト

また、事業内容は現在のページに準拠するということで、現在サイトのパスはpemixとなります。

TOPページへの掲載内容については、
TOPイメージ
事業内容
採用情報
新着情報
となります。
サイトURL
http://nexal.co.jp/
ページ数
1ページ
希望イメージ
シンプル 複雑
単色 カラフル
暗い 明るい
日常 高級
遊び心 厳粛
未来的 伝統的
女性的 男性的
希望する色
緑系
納品ファイル
• フォトショップ形式 (.psd)
補足説明
依頼公開後の追記内容
現行サイトのパスワードについて失念しておりました。
パスワードは pemix となります。
■ 選んだ理由

デザインが特に先方に気に入られたため

■ 提案者全員のお礼・コメント

この度はご提案をいただきまして、誠にありがとうございました。
また機会がありましたら、よろしくお願い致します。

```html
<!DOCTYPE html>
<html lang="ja">
<head>
<meta charset="utf-8">
<title>NEXAL</title>
<link rel="stylesheet" href="https://fonts.googleapis.com/css2?family=Montserrat:wght@500;700;800&family=Noto+Sans+JP:wght@400;500;700&display=swap">
<style>
:root{
  --green:#3a9a2a;
  --green-bright:#5bb531;
  --green-dark:#23421c;
  --ink:#222;
  --muted:#666;
  --pale:#eef2ee;
  --white:#fff;
}
*{margin:0;padding:0;box-sizing:border-box}
html,body{width:1200px;height:3124px;overflow:hidden}
body{position:relative;background:var(--white);font-family:"Noto Sans JP",sans-serif;color:var(--ink)}
.abs{position:absolute}
.en{font-family:"Montserrat",sans-serif}

/* hero */
.hero{left:0;top:0;width:1200px;height:680px;background:linear-gradient(90deg,#3f9a22 0%,#6cba3a 45%,#b9d9a3 70%,#dfe9d6 100%)}
.hero-photo{left:600px;top:0;width:600px;height:680px;background:linear-gradient(90deg,rgba(255,255,255,0) 0%,rgba(40,50,60,.22) 60%,rgba(30,40,50,.28) 100%)}
.logo{left:48px;top:20px;color:var(--white);font-size:34px;font-weight:800;letter-spacing:2px}
.nav{right:40px;top:24px;display:flex;align-items:center;gap:36px;color:var(--white);font-size:15px;font-weight:500}
.nav .contact{border:2px solid var(--white);padding:8px 20px}
.hero-title{left:112px;top:236px;color:var(--white);font-size:46px;font-weight:700;line-height:64px}
.hero-sub{left:112px;top:480px;color:var(--white);font-size:20px;letter-spacing:2px}

/* section headings */
.heading{left:0;width:1200px;text-align:center}
.heading h2{font-family:"Montserrat",sans-serif;font-size:30px;font-weight:700;display:inline-block;padding:0 24px 10px;border-bottom:2px solid currentColor}
.heading p{font-size:13px;margin-top:8px}

/* business */
.biz-bg{left:272px;top:680px;width:928px;height:1080px;background:var(--pale)}
.photo{background:linear-gradient(135deg,#c9c2b0,#9aa8a0)}
.card{background:var(--white);box-shadow:0 6px 24px rgba(0,0,0,.15);padding:44px 48px}
.card h3{font-family:"Montserrat",sans-serif;color:var(--green);font-size:38px;font-weight:700;line-height:42px}
.card .jp{font-size:15px;font-weight:700;border-bottom:2px solid var(--ink);display:inline-block;padding-bottom:6px;margin:6px 0 20px;width:100%}
.card .body{font-size:14px;line-height:24px;color:var(--muted)}
.btn-more{display:inline-block;background:var(--ink);color:var(--white);font-family:"Montserrat",sans-serif;font-size:12px;font-weight:700;letter-spacing:1px;padding:7px 44px;margin-top:24px}

/* recruit */
.recruit-band{left:0;top:1760px;width:1200px;height:260px;background:linear-gradient(180deg,#2f2f2f,#4a4a4a)}
.btn-green{display:inline-block;background:var(--green);color:var(--white);font-size:13px;font-weight:700;padding:8px 28px;margin-top:24px;margin-right:16px}

/* news */
.news-list{left:280px;top:2440px;width:640px}
.news-row{display:flex;align-items:center;height:64px;border-bottom:1px solid #ddd;font-size:14px}
.news-row .date{width:192px}
.news-row .tag{background:var(--green);color:var(--white);font-size:12px;padding:4px 0;width:100px;text-align:center;margin-right:28px}
.news-more{left:0;top:2684px;width:1200px;text-align:center}

/* footer */
.footer{left:0;top:2800px;width:1200px;height:324px;background:var(--green-dark)}
.footer-text{color:var(--white)}
.f-logo{left:108px;top:2840px;font-size:34px;font-weight:800;letter-spacing:2px}
.f-name{left:108px;top:2892px;font-size:15px;font-weight:700}
.f-addr{left:108px;top:2930px;font-size:13px;line-height:24px}
.f-contact{left:860px;top:2886px;width:160px;background:var(--green-bright);text-align:center;font-size:14px;font-weight:700;padding:10px 0}
.f-links{left:860px;top:2942px;width:160px;text-align:right;font-size:14px;line-height:34px}
.f-rule{left:0;top:3070px;width:1200px;height:1px;background:rgba(255,255,255,.25)}
.f-copy{left:0;top:3090px;width:1200px;text-align:center;font-size:12px;font-family:"Montserrat",sans-serif}
</style>
</head>
<body>

<header>
  <div class="abs hero"></div>
  <div class="abs hero-photo" role="img" aria-label="スーツ姿の男性がファイルを持って立つ写真"></div>
  <div class="abs logo en">NEXAL</div>
  <nav class="abs nav">
    <span>事業紹介</span><span>採用情報</span><span>新着情報</span><span class="contact">お問い合わせ</span>
  </nav>
  <h1 class="abs hero-title en">Uniting Intelligence<br>into Curiosity and<br>Courage brings Eternality</h1>
  <p class="abs hero-sub">好奇心と勇気に知恵を結び付ければ、可能性も永続につながる</p>
</header>

<section>
  <div class="abs biz-bg"></div>
  <div class="abs heading" style="top:740px"><h2>Business</h2><p>事業内容</p></div>

  <div class="abs photo" style="left:108px;top:860px;width:572px;height:340px;background:linear-gradient(135deg,#e8dcc4,#b8a88c)" role="img" aria-label="机で勉強する子どもたちの写真"></div>
  <div class="abs card" style="left:660px;top:888px;width:480px;height:288px">
    <h3>Education<br>Division</h3>
    <div class="jp">教育事業部</div>
    <p class="body">テキストテキストテキストテキストテキストテキストテキストテキストテキストテキストテキストテキスト</p>
    <span class="btn-more">MORE</span>
  </div>

  <div class="abs photo" style="left:188px;top:1268px;width:572px;height:340px;background:linear-gradient(180deg,#b9cbd8,#8a8f86 55%,#6f7466)" role="img" aria-label="車が行き交う都市の大通りの写真"></div>
  <div class="abs card" style="left:740px;top:1292px;width:360px;height:300px">
    <h3>Nitai<br>Division</h3>
    <div class="jp">日泰事業部</div>
    <p class="body">テキストテキストテキストテキストテキストテキストテキストテキスト</p>
    <span class="btn-more">MORE</span>
  </div>
</section>

<section>
  <div class="abs recruit-band" role="img" aria-label="会議室の写真を暗く重ねた背景"></div>
  <div class="abs heading" style="top:1810px;color:var(--white)"><h2>Recruit</h2><p>採用情報</p></div>
  <div class="abs photo" style="left:108px;top:1932px;width:484px;height:308px;background:linear-gradient(135deg,#d9d9d9,#9c9c9c)" role="img" aria-label="職場で話すスタッフの写真"></div>
  <div class="abs card" style="left:592px;top:1932px;width:500px;height:296px">
    <div class="jp" style="font-size:22px;margin-top:0">求めるNEXAL人材</div>
    <p class="body">テキストテキストテキストテキストテキストテキストテキストテキストテキストテキストテキストテキスト</p>
    <span class="btn-green">採用情報はこちら</span><span class="btn-more">MORE</span>
  </div>
</section>

<section>
  <div class="abs heading" style="top:2330px"><h2>News</h2><p>新着情報</p></div>
  <div class="abs news-list">
    <div class="news-row"><span class="date">2022.02.01</span><span class="tag">お知らせ</span><span>テキストテキストテキストテキストテキスト</span></div>
    <div class="news-row"><span class="date">2022.02.01</span><span class="tag">お知らせ</span><span>テキストテキストテキストテキストテキスト</span></div>
    <div class="news-row"><span class="date">2022.02.01</span><span class="tag">お知らせ</span><span>テキストテキストテキストテキストテキスト</span></div>
  </div>
  <div class="abs news-more"><span class="btn-more" style="margin-top:0">MORE</span></div>
</section>

<footer>
  <div class="abs footer"></div>
  <div class="abs footer-text f-logo en">NEXAL</div>
  <div class="abs footer-text f-name">株式会社ネクサル</div>
  <div class="abs footer-text f-addr">〒000-0000<br>滋賀県大津市架空町1-2-3<br>サンプルビル5F<br>TEL：000-000-0000<br>FAX：000-000-0000</div>
  <div class="abs footer-text f-contact">お問い合わせ</div>
  <div class="abs footer-text f-links">事業案内<br>採用情報<br>新着情報</div>
  <div class="abs f-rule"></div>
  <div class="abs footer-text f-copy">© NEXAL Co.,Ltd.</div>
</footer>

</body>
</html>
```